Kestrel Ark AI Power Point Pitch Deck Design

We are in need of building out a designed version of the attached Power Point. We are a SaaS company focused on utilizing AI to perform marketing functions for small to medium sized businesses. We are looking for a modern SaaS design for this pitch deck.

I have included a mock up of a design for our logo we are thinking of using, we may change the colors but let's go forward with this scheme as shown. We are looking for a matured design here so on places where we use statistics ways to make the statistics pop graphically. Interesting ways to display the information from slide to slide so it doesn't feel repetitive.

Generally speaking this should feel polished enough for us to go to VC firms to raise money. Happy to answer additional questions.

Target Market(s)

VC's

Industry/Entity Type

SaaS

Font styles to use
Sans Serif

Requirements
Must have
• A complete design that feels branded to an AI SaaS
Nice to have
• I'd like graphics within the deck that highlight various statistics
Should not have
• Should not feel cartoon like. It should be professional and modern

```html
<!DOCTYPE html>
<html lang="en">
<head>
<meta charset="utf-8">
<title>Kestrel Ark AI – Pitch Deck Overview</title>
<link href="https://fonts.googleapis.com/css2?family=Fira+Sans:wght@500;600&family=Poppins:wght@400;500;600&display=swap" rel="stylesheet">
<style>
  :root{
    --teal:#12e0b2;
    --navy:#0f0c5c;
    --purple:#8b45e6;
    --ink:#2b2b33;
    --muted:#4a4a55;
    --red:#d8322e;
    --blue:#1b4fa8;
    --paper:#ffffff;
  }
  *{box-sizing:border-box;margin:0;padding:0}
  html,body{width:939px;height:1200px;overflow:hidden;background:var(--paper)}
  body{position:relative;font-family:"Poppins",sans-serif;color:var(--ink)}
  .slide{position:absolute;width:396px;height:223px;background:#fff;overflow:hidden;box-shadow:0 4px 10px rgba(0,0,0,.16)}
  .col-l{left:52px}.col-r{left:495px}
  .row-1{top:59px}.row-2{top:346px}.row-3{top:632px}.row-4{top:919px}
  .abs{position:absolute}

  /* brand lockup */
  .brand{position:absolute;top:7px;right:4px;text-align:right;line-height:1}
  .brand-name{font-family:"Fira Sans",sans-serif;font-weight:500;font-size:10px;letter-spacing:.5px;color:var(--navy)}
  .brand-sub{font-family:"Fira Sans",sans-serif;font-weight:500;font-size:5px;letter-spacing:2.4px;color:var(--purple);margin-top:1px}
  .brand.light .brand-name,.brand.light .brand-sub{color:#fff}

  /* footer */
  .footer{position:absolute;left:0;right:28px;bottom:3px;height:12px;background:var(--teal);display:flex;align-items:center}
  .globe{width:12px;height:12px;background:var(--navy);display:flex;align-items:center;justify-content:center;margin-left:6px}
  .url{font-size:4.6px;color:var(--navy);margin-left:5px}
  .page-no{position:absolute;right:0;bottom:3px;width:26px;height:13px;background:var(--navy);color:#fff;font-size:4.4px;display:flex;align-items:center;justify-content:center}

  /* titles & text */
  .title{font-family:"Fira Sans",sans-serif;font-weight:600;color:var(--navy);font-size:11px;border-left:1px solid var(--purple);padding-left:7px;line-height:1.2;white-space:nowrap}
  .head{font-family:"Fira Sans",sans-serif;font-weight:600;font-size:5.8px;color:var(--navy)}
  .sub{font-weight:500;font-size:5px;color:var(--ink)}
  .body{font-size:4.7px;line-height:1.85;color:var(--muted)}
  .dot-list{list-style:none}
  .dot-list > li{position:relative;padding-left:9px}
  .dot-list > li::before{content:"";position:absolute;left:0;top:2px;width:3px;height:3px;border-radius:50%;background:var(--purple)}
  .ring-list{list-style:none}
  .ring-list li{position:relative;padding-left:7px}
  .ring-list li::before{content:"";position:absolute;left:0;top:2.5px;width:2.4px;height:2.4px;border-radius:50%;border:.6px solid var(--purple)}
  .photo{position:absolute}

  /* cover */
  .cover-bg{position:absolute;inset:0;background:linear-gradient(120deg,#eef1f2 0%,#f7f8f8 50%,#e9ecef 100%)}
  .cover-brand{position:absolute;left:14px;top:92px;line-height:1}
  .cover-brand .brand-name{font-size:30px;letter-spacing:1px}
  .cover-brand .brand-sub{font-size:14px;letter-spacing:9px;text-align:right;margin-top:4px}
  .cover-foot{position:absolute;left:0;right:0;bottom:0;height:13px;background:var(--teal);font-size:4.4px;color:var(--ink);display:flex;align-items:center;justify-content:center}

  /* timeline list on landscape slide */
  .timeline{position:absolute;left:195px;top:73px;width:170px;border-left:.5px solid #8a8ab0;padding-left:7px}
  .timeline .item{position:relative;margin-bottom:9px}
  .timeline .item::before{content:"";position:absolute;left:-9px;top:2px;width:3px;height:3px;border-radius:50%;background:var(--purple)}

  /* vantor slide */
  .vantor-name{position:absolute;top:10px;right:7px;font-family:"Fira Sans",sans-serif;font-weight:600;font-size:14px;color:var(--blue)}
  .red-list{list-style:none;font-size:5.3px;color:var(--ink)}
  .red-list li{position:relative;padding-left:5px;margin-bottom:10px}
  .red-list li::before{content:"";position:absolute;left:0;top:2.2px;width:2.4px;height:2.4px;border-radius:50%;background:var(--red)}
  .v-foot-url{position:absolute;left:0;bottom:4px;width:67px;height:12px;background:var(--blue);display:flex;align-items:center}
  .v-foot-url .globe{background:transparent;margin-left:5px}
  .v-foot-url .url{color:#fff}
  .v-copy{position:absolute;left:0;right:0;bottom:6px;text-align:center;font-size:4.4px}
  .v-page{position:absolute;right:0;bottom:5px;width:24px;height:12px;background:var(--red);color:#fff;font-size:4.4px;display:flex;align-items:center;justify-content:center}
</style>
</head>
<body>

<!-- Cover -->
<section class="slide col-l row-1">
  <div class="cover-bg" role="img" aria-label="Faded office photo of a team at work"></div>
  <div class="cover-brand">
    <div class="brand-name">KESTREL ARK</div>
    <div class="brand-sub">AI</div>
  </div>
  <div class="cover-foot">© 2024. All Rights Reserved.</div>
</section>

<!-- Landscape -->
<section class="slide col-r row-1">
  <div class="brand"><div class="brand-name">KESTREL ARK</div><div class="brand-sub">AI</div></div>
  <svg class="photo" style="left:27px;top:22px" width="142" height="172" viewBox="0 0 142 172" role="img" aria-label="Business people shaking hands in an office">
    <defs><linearGradient id="hexA" x1="0" y1="0" x2="1" y2="1"><stop offset="0" stop-color="#b9c4c8"/><stop offset=".6" stop-color="#7d8a8c"/><stop offset="1" stop-color="#4e5a5c"/></linearGradient></defs>
    <polygon points="71,2 139,42 139,130 71,170 3,130 3,42" fill="url(#hexA)" stroke="var(--teal)" stroke-width="3"/>
  </svg>
  <div class="title abs" style="left:185px;top:52px">The Current B2B SMB Landscape</div>
  <div class="timeline">
    <div class="item"><div class="head">3.9 Million SMBs:</div><p class="body" style="padding-left:8px">There are 3.9 million small and medium-sized<br>businesses in the United States.</p></div>
    <div class="item"><div class="head">Challenges in Growth:</div><p class="body" style="padding-left:8px">Many of these businesses are striving to grow and<br>compete against massive competitors.</p></div>
    <div class="item"><div class="head">The Digital Marketing Disadvantage:</div><p class="body" style="padding-left:8px">Digital marketing is tasked with leading their growth<br>efforts, but SMBs are at a distinct disadvantage due to<br>limited resources and expertise.</p></div>
  </div>
  <div class="footer"><span class="globe"><svg width="8" height="8" viewBox="0 0 10 10"><g fill="none" stroke="#fff" stroke-width=".8"><circle cx="5" cy="5" r="4"/><ellipse cx="5" cy="5" rx="1.8" ry="4"/><path d="M1 5h8M1.6 3h6.8M1.6 7h6.8"/></g></svg></span><span class="url">www.kestrelarkai.com</span></div>
  <div class="page-no">Page 02</div>
</section>

<!-- Introducing -->
<section class="slide col-l row-2">
  <div class="photo" style="left:0;top:0;width:396px;height:155px;background:linear-gradient(100deg,#6b4a2c 0%,#b98a55 30%,#d9b98f 50%,#5c4a3a 75%,#2f2a28 100%)" role="img" aria-label="Team celebrating a win around a laptop"></div>
  <div class="brand light"><div class="brand-name">KESTREL ARK</div><div class="brand-sub">AI</div></div>
  <div class="title abs" style="left:122px;top:161px">Introducing Kestrel Ark AI</div>
  <p class="body abs" style="left:0;right:0;top:182px;text-align:center">A marketerless marketing agency, powered by AI, to deliver top-tier strategy and campaign execution<br>with the efficiency and margins of a software company.</p>
  <div class="footer"><span class="globe"><svg width="8" height="8" viewBox="0 0 10 10"><g fill="none" stroke="#fff" stroke-width=".8"><circle cx="5" cy="5" r="4"/><ellipse cx="5" cy="5" rx="1.8" ry="4"/><path d="M1 5h8M1.6 3h6.8M1.6 7h6.8"/></g></svg></span><span class="url">www.kestrelarkai.com</span></div>
  <div class="page-no">Page 04</div>
</section>

<!-- Unique approach -->
<section class="slide col-r row-2">
  <div class="brand"><div class="brand-name">KESTREL ARK</div><div class="brand-sub">AI</div></div>
  <div class="title abs" style="left:27px;top:8px">Our Unique Approach</div>
  <ul class="dot-list abs" style="left:35px;top:26px;width:162px">
    <li style="margin-bottom:6px"><div class="head">Generates Complete Marketing Plans:</div>
      <ul class="ring-list body"><li>Develop effective strategies for marketing to the specific client's ideal customers profile.</li></ul></li>
    <li style="margin-bottom:6px"><div class="head">Guided Execution with Project Management:</div>
      <ul class="ring-list body"><li>The project management tool lays out all the pieces for execution.</li><li>Guides users step-by-step through creating each piece of the marketing strategy utilizing specially trained AI for each specific task.</li></ul></li>
    <li style="margin-bottom:6px"><div class="head">Implementation and Deployment:</div>
      <ul class="ring-list body"><li>Connects to platforms used for running campaigns to deploy content seamlessly. Tracks results and feeds them back into the strategy environment.</li></ul></li>
    <li><div class="head">Continuous Improvement:</div>
      <ul class="ring-list body"><li>AI analyzes campaign results against set goals. Adjusts strategies for future campaigns to continuously improve results.</li></ul></li>
  </ul>
  <div class="abs" style="left:222px;top:126px;width:84px;height:55px;border-left:1px dotted var(--navy);border-bottom:1px dotted var(--navy)"></div>
  <div class="abs" style="left:309px;top:44px;width:60px;height:44px;background:var(--navy)"></div>
  <div class="photo" style="left:230px;top:51px;width:132px;height:125px;background:linear-gradient(135deg,#9aa4a8 0%,#d6dadb 50%,#8e8a84 100%)" role="img" aria-label="Two colleagues shaking hands across a meeting table"></div>
  <div class="footer"><span class="globe"><svg width="8" height="8" viewBox="0 0 10 10"><g fill="none" stroke="#fff" stroke-width=".8"><circle cx="5" cy="5" r="4"/><ellipse cx="5" cy="5" rx="1.8" ry="4"/><path d="M1 5h8M1.6 3h6.8M1.6 7h6.8"/></g></svg></span><span class="url">www.kestrelarkai.com</span></div>
  <div class="page-no">Page 05</div>
</section>

<!-- Key emphasis (partner template) -->
<section class="slide col-l row-3">
  <div class="vantor-name">Vantor</div>
  <div class="photo" style="left:12px;top:39px;width:82px;height:114px;border-radius:22px 0 22px 0;background:linear-gradient(160deg,#8d9aa6,#d7dde2 55%,#d3a437)" role="img" aria-label="Hands reviewing team charts on a desk"></div>
  <div class="photo" style="left:100px;top:62px;width:83px;height:115px;border-radius:22px 0 22px 0;background:linear-gradient(160deg,#e9e9e9,#9b9b9b 55%,#d9d9d9)" role="img" aria-label="Person signing a document with a pen"></div>
  <div class="abs" style="left:197px;top:72px;font-family:'Fira Sans',sans-serif;font-weight:600;font-size:9px;color:var(--ink)">Key Emphasis</div>
  <ul class="red-list abs" style="left:197px;top:99px">
    <li>80 to 90% sales is done through agents</li>
    <li>Company performance highly dependent on the agents</li>
    <li>No integrated platform to manage agent cycle</li>
  </ul>
  <div class="v-foot-url"><span class="globe"><svg width="8" height="8" viewBox="0 0 10 10"><g fill="none" stroke="#fff" stroke-width=".8"><circle cx="5" cy="5" r="4"/><ellipse cx="5" cy="5" rx="1.8" ry="4"/><path d="M1 5h8M1.6 3h6.8M1.6 7h6.8"/></g></svg></span><span class="url">www.vantorgroup.com</span></div>
  <div class="v-copy">© 2024. All Rights Reserved.</div>
  <div class="v-page">Page 06</div>
</section>

<!-- Funding -->
<section class="slide col-r row-3">
  <div class="brand"><div class="brand-name">KESTREL ARK</div><div class="brand-sub">AI</div></div>
  <div class="title abs" style="left:24px;top:19px">Utilization of Funding</div>
  <ul class="dot-list abs" style="left:28px;top:40px;width:160px">
    <li><div class="head">Ramp Up Engineering:</div>
      <div class="sub" style="margin-top:5px">API Development:</div>
      <ul class="ring-list body"><li>Focus on building APIs for seamless integration with various marketing platforms, simplifying the implementation of campaign outputs.</li></ul>
      <div class="sub" style="margin-top:5px">Analysis Tool:</div>
      <ul class="ring-list body"><li>Develop an advanced analysis tool using these APIs, enabling real-time data tracking and insights. This feature will unlock a higher price point for our offerings, providing additional value to clients.</li></ul>
      <div class="sub" style="margin-top:5px">UI/UX Development:</div>
      <ul class="ring-list body"><li>Prioritize creating a simple and intuitive platform specifically for marketers, ensuring minimal friction and a smooth user experience to prevent abandonment.</li></ul>
    </li>
  </ul>
  <ul class="dot-list abs" style="left:215px;top:40px;width:160px">
    <li><div class="head">Invest in Sales and Marketing:</div>
      <div class="sub" style="margin-top:5px">Founder-Led Sales:</div>
      <ul class="ring-list body"><li>Initially, sales efforts will be led by Dana Whitcombe, leveraging his experience in running sales and marketing at a successful marketing agency. His expertise will be instrumental in driving early-stage growth and market penetration.</li></ul>
      <div class="sub" style="margin-top:12px">Marketing Campaigns:</div>
      <ul class="ring-list body"><li>Allocate funds for impactful marketing campaigns to attract and convert users. The goal is to drive user growth and effectively transition free users into paying customers, maximizing revenue potential.</li></ul>
    </li>
  </ul>
  <div class="footer"><span class="globe"><svg width="8" height="8" viewBox="0 0 10 10"><g fill="none" stroke="#fff" stroke-width=".8"><circle cx="5" cy="5" r="4"/><ellipse cx="5" cy="5" rx="1.8" ry="4"/><path d="M1 5h8M1.6 3h6.8M1.6 7h6.8"/></g></svg></span><span class="url">www.kestrelarkai.com</span></div>
  <div class="page-no">Page 08</div>
</section>

<!-- Problem -->
<section class="slide col-l row-4">
  <div class="brand"><div class="brand-name">KESTREL ARK</div><div class="brand-sub">AI</div></div>
  <div class="title abs" style="left:12px;top:52px">The Problem with SMB Marketing</div>
  <ul class="dot-list body abs" style="left:23px;top:81px;width:160px;line-height:1.85">
    <li style="margin-bottom:8px">SMBs are spending $90 billion annually on marketing efforts but are not achieving the growth they need.</li>
    <li style="margin-bottom:8px">Agencies, while a necessary resource due to lack of internal expertise, often prove to be ineffective and</li>
    <li style="margin-bottom:8px">According to a Marketpulse poll, 63% of SMBs say generating traffic and leads is their hardest challenge.</li>
    <li>With smaller budgets as a whole, they often spend a disproportionate amount on the agency instead of media buys.</li>
  </ul>
  <svg class="photo" style="left:196px;top:16px" width="162" height="192" viewBox="0 0 162 192" role="img" aria-label="Collage of business team meeting photos in hexagon frames">
    <defs><linearGradient id="hexB" x1="0" y1="0" x2="1" y2="1"><stop offset="0" stop-color="#c9c2b8"/><stop offset="1" stop-color="#6d645c"/></linearGradient>
    <linearGradient id="hexC" x1="0" y1="0" x2="1" y2="1"><stop offset="0" stop-color="#3d6fa8"/><stop offset="1" stop-color="#0f2c5a"/></linearGradient></defs>
    <polygon points="20,0 38,10 38,30 20,40 2,30 2,10" fill="url(#hexB)"/>
    <polygon points="36,34 54,44 54,64 36,74 18,64 18,44" fill="url(#hexB)"/>
    <polygon points="100,0 138,22 138,66 100,88 62,66 62,22" fill="url(#hexB)"/>
    <polygon points="62,82 99,103 99,147 62,168 25,147 25,103" fill="url(#hexB)"/>
    <polygon points="128,84 150,97 150,123 128,136 106,123 106,97" fill="url(#hexC)"/>
    <polygon points="98,135 112,143 112,159 98,167 84,159 84,143" fill="url(#hexB)"/>
    <polygon points="112,158 126,166 126,182 112,190 98,182 98,166" fill="url(#hexB)"/>
  </svg>
  <div class="footer"><span class="globe"><svg width="8" height="8" viewBox="0 0 10 10"><g fill="none" stroke="#fff" stroke-width=".8"><circle cx="5" cy="5" r="4"/><ellipse cx="5" cy="5" rx="1.8" ry="4"/><path d="M1 5h8M1.6 3h6.8M1.6 7h6.8"/></g></svg></span><span class="url">www.kestrelarkai.com</span></div>
  <div class="page-no">Page 03</div>
</section>

<!-- How it works -->
<section class="slide col-r row-4">
  <div class="brand"><div class="brand-name">KESTREL ARK</div><div class="brand-sub">AI</div></div>
  <div class="title abs" style="left:130px;top:19px">How Kestrel Ark AI Works</div>
  <div class="abs" style="left:29px;top:50px;width:152px">
    <div class="head">Rapid Onboarding:</div>
    <ul class="ring-list body" style="margin-top:2px"><li style="margin-bottom:2px">We walk you through a typical agency onboarding in minutes, a process that usually takes weeks.</li><li>Analyze your current website and develop a marketing plan with specific strategies for reaching your goals.</li></ul>
    <div class="head" style="margin-top:12px">Output Creation:</div>
    <ul class="ring-list body" style="margin-top:2px"><li style="margin-bottom:2px">Combines content creation, SEO, and paid search offerings.</li><li style="margin-bottom:2px">Our project management tool guides users through all the pieces and nuances.</li><li>Leverages highly trained AI agents specific to each task, making specialized marketer expertise accessible.</li></ul>
  </div>
  <div class="abs" style="left:216px;top:50px;width:152px">
    <div class="head">Implementation:</div>
    <ul class="ring-list body" style="margin-top:2px"><li style="margin-bottom:2px">Provides AI agent support on how to implement these assets on various platforms in a guided experience.</li><li>Alternatively, users can integrate those platforms with our tool and allow our API to push the outputs directly.</li></ul>
    <div class="head" style="margin-top:12px">Reporting and Analysis:</div>
    <ul class="ring-list body" style="margin-top:2px"><li style="margin-bottom:2px">For the first time ever, our platform aggregates all the data back to a singular place.</li><li style="margin-bottom:2px">Judges performance using AI against the original strategy.</li><li>Utilizes the data to make improvements to the plan, increasing effectiveness for the next campaigns.</li></ul>
  </div>
  <div class="footer"><span class="globe"><svg width="8" height="8" viewBox="0 0 10 10"><g fill="none" stroke="#fff" stroke-width=".8"><circle cx="5" cy="5" r="4"/><ellipse cx="5" cy="5" rx="1.8" ry="4"/><path d="M1 5h8M1.6 3h6.8M1.6 7h6.8"/></g></svg></span><span class="url">www.kestrelarkai.com</span></div>
  <div class="page-no">Page 06</div>
</section>

</body>
</html>
```